Varelio Soins: Symposium annuel 2018

You created the flyer "Atelier des pairs" for us at the beginning of the year. We would like to work in a new version. More details can be found in the briefing! Flyer (red, gray, black) - flyer wants to be white! - Flyer wants to be White! All further information can be found in the document in the appendix!

```html
<!DOCTYPE html>
<html lang="fr">
<head>
<meta charset="utf-8">
<title>Varelio Soins – Atelier des pairs</title>
<link rel="stylesheet" href="https://fonts.googleapis.com/css2?family=Bebas+Neue&family=Montserrat:wght@400;500;700&display=swap">
<style>
  :root {
    --red: #e1000f;
    --black: #111111;
    --grey-line: #c9c9c9;
    --grey-soft: #ededed;
    --grey-mid: #8a8a8a;
    --navy: #14264a;
    --white: #ffffff;
  }
  * { margin: 0; padding: 0; box-sizing: border-box; }
  html, body { width: 1200px; height: 1200px; overflow: hidden; background: var(--white); }
  body { position: relative; font-family: "Montserrat", sans-serif; color: var(--black); }

  .card { position: absolute; left: 249px; width: 711px; height: 502px; overflow: hidden; background: var(--white); outline: 1px solid #eeeeee; }
  .card--front { top: 58px; background: linear-gradient(135deg, #f4f4f4, #e9e9e9 60%, #f2f2f2); }
  .card--back { top: 608px; }

  /* front */
  .network-ring { position: absolute; inset: 0;
    background: radial-gradient(ellipse 34% 44% at 50% 49%, #fafafa 0 62%, #cfcfcf 74%, #bdbdbd 80%, #dedede 90%, transparent 100%); }
  .front-title { position: absolute; left: 0; right: 0; text-align: center; font-family: "Bebas Neue", sans-serif; line-height: 0.95; }
  .front-title__red { top: 152px; font-size: 56px; color: var(--red); }
  .front-title__black { top: 202px; font-size: 56px; color: var(--black); }
  .front-date { position: absolute; top: 277px; left: 0; right: 0; text-align: center; font-family: "Bebas Neue", sans-serif; font-size: 27px; color: var(--red); }
  .brand { position: absolute; top: 336px; left: 0; right: 0; display: flex; justify-content: center; align-items: center; gap: 7px; }
  .brand__mark { width: 20px; height: 20px; background: var(--black); }
  .brand__name { font-family: "Montserrat", sans-serif; font-weight: 700; font-size: 19px; letter-spacing: 1px; color: var(--black); }

  /* back */
  .molecules { position: absolute; right: 0; top: 0; width: 320px; height: 320px;
    background: radial-gradient(circle at 78% 28%, #e6e6e6 0, #f1f1f1 40%, rgba(255,255,255,0) 72%); }
  .back-title { position: absolute; left: 34px; top: 24px; font-family: "Bebas Neue", sans-serif; font-size: 50px; line-height: 1; color: var(--black); white-space: nowrap; }
  .back-title .accent { color: var(--red); }
  .title-rule { position: absolute; left: 34px; top: 78px; width: 303px; height: 1px; background: var(--grey-mid); }
  .back-date { position: absolute; left: 35px; top: 83px; font-weight: 700; font-size: 29px; color: var(--black); }
  .back-date .accent { color: var(--red); }
  .back-time { position: absolute; left: 35px; top: 120px; font-family: "Bebas Neue", sans-serif; font-size: 25px; color: var(--red); }

  .info-table { position: absolute; left: 34px; top: 154px; width: 653px; border-top: 1px solid var(--grey-line); }
  .info-row { display: flex; align-items: center; border-bottom: 1px solid var(--grey-line); }
  .info-row__label { width: 179px; padding-left: 11px; font-weight: 500; font-size: 16px; color: var(--red); }
  .info-row__value { flex: 1; font-size: 11.5px; line-height: 1.25; padding-right: 6px; }
  .row-lieu { height: 33px; }
  .row-dest { height: 42px; }
  .row-prog { height: 58px; }
  .row-prix { height: 53px; }
  .row-prix .info-row__value p + p { margin-top: 7px; }
  .row-delai { height: 45px; border-bottom: none; }

  .contact-band { position: absolute; left: 34px; top: 387px; width: 653px; height: 29px; background: var(--red); color: var(--white); border-radius: 2px; display: flex; align-items: center; justify-content: center; font-size: 15px; }
  .contact-band strong { font-weight: 700; margin-left: 4px; }
  .partners-title { position: absolute; top: 423px; left: 0; right: 0; text-align: center; font-size: 14px; letter-spacing: 0.5px; }
  .partners { position: absolute; left: 40px; top: 452px; width: 640px; display: flex; justify-content: space-between; align-items: center; }
  .partner-badge { height: 22px; background: #d8d8d8; border-radius: 2px; }
  .partner-badge--a { width: 92px; background: #2a4a8c; }
  .partner-badge--b { width: 92px; background: #c9d3e6; }
  .partner-badge--c { width: 108px; background: #e4d8ea; }
  .partner-badge--d { width: 124px; background: #dbeadb; }
  .partner-badge--e { width: 64px; height: 38px; background: var(--navy); }
</style>
</head>
<body>

<section class="card card--front">
  <div class="network-ring" role="img" aria-label="Anneau décoratif de points reliés par des lignes fines en gris"></div>
  <div class="front-title front-title__red">Atelier</div>
  <div class="front-title front-title__black">Des pairs</div>
  <div class="front-date">21 avril 2018</div>
  <div class="brand">
    <span class="brand__mark"></span>
    <span class="brand__name">VARELIO SOINS</span>
  </div>
</section>

<section class="card card--back">
  <div class="molecules" role="img" aria-label="Motif décoratif léger de molécules grises"></div>
  <h1 class="back-title"><span class="accent">ATELIER</span> DES PAIRS</h1>
  <div class="title-rule"></div>
  <div class="back-date">21 avril <span class="accent">2018</span></div>
  <div class="back-time">9H00 - 14H00</div>

  <div class="info-table">
    <div class="info-row row-lieu">
      <div class="info-row__label">Lieu</div>
      <div class="info-row__value">Auditoire Marceline Roux (PSR) HUVM, Montreuse</div>
    </div>
    <div class="info-row row-dest">
      <div class="info-row__label">Destinateur</div>
      <div class="info-row__value">Physiothérapeutes, Lymphothérapeute</div>
    </div>
    <div class="info-row row-prog">
      <div class="info-row__label">Programme</div>
      <div class="info-row__value">après une introduction sur les actualités dans la prise en charge des pathologies lymphatique nous organisons des ateliers pratique (drainage, bandage, compression élastique, les outils etc.)</div>
    </div>
    <div class="info-row row-prix">
      <div class="info-row__label">Prix</div>
      <div class="info-row__value"><p>CHF 100.-</p><p>CHF 50.- (pour les membres de Varelio Soins)</p></div>
    </div>
    <div class="info-row row-delai">
      <div class="info-row__label">Délai d’inscription</div>
      <div class="info-row__value">15 mars 2018 (limitation de place, max 80 participants)</div>
    </div>
  </div>

  <div class="contact-band">Inscription et renseignement via email : <strong>info@varelio-soins.ch</strong></div>
  <div class="partners-title">PARTENAIRS</div>
  <div class="partners">
    <span class="partner-badge partner-badge--a"></span>
    <span class="partner-badge partner-badge--b"></span>
    <span class="partner-badge partner-badge--c"></span>
    <span class="partner-badge partner-badge--d"></span>
    <span class="partner-badge partner-badge--e"></span>
  </div>
</section>

</body>
</html>
```